Health care finance company startup website design

This design brief is for Ledger Loom, a small start-up company dealing with an online health care (initially dental targeted with plans for medical market) financial suite of tools. My business partners and I are looking to have a website developed for our business model.

We have developed a professional logo and would like it incorporated into the site. We are open to modifications on the logo if needed to accomplish the right design.

Our concept is a clean, simple design with a professional polish and very up-to-date web presence. The functionality of the site is simple yet powerful and we would like it’s design to complement that (including anticipated css3/html5 effects for an added dimension of UI polish).

We would like to see a design mockup of the functional elements of our site as our home page. We would also be very interested to see how your design would flow into the other pages such as search for a loan, create a payment plan, make a payment, sign in, registration, contact us and learn more.

Regarding Functional Elements:

-Simplicity is king.

-The three main functions of the site are the focus. They will operate via a series of API’s to webservices on the back-end, making the front end field focused, though we hope to have it feel friendly and simple.
-Search for a loan
-Create a payment plan
-Make a payment

Other functions of the site include:

-Sign in module
-We plan to support Kindred Link, Vortal Verify and PassGate so incorporating design for those options is a plus.

-Registration module
-Two service levels clients can register for, loans only or loans & payments
-The registration process should be divided into sections with navigation back and forth until a confirmation final screen with pdf generations and remaining “to-do items” listed.
-The registration information will be saved in our database and also auto-populate fields for PDF’s that will be generated from templates.
-The registration will send a confirmation email and support PassGate, Vortal Verify and Kindred Link, so designs should take these programmatic features into account.

-Contact us
-This will emphasize digital forms of communication (email and form submitted contact request).

-Learn more
-Explanations/faqs/tutorials
-This will contain video demonstrations/screencasts of key functions of website features

Regarding Design Elements:
-We want to be “wow’d” and don’t mind a surprise that redefines what we thought we liked regarding design.
-The following examples indicate some of the color schemes we like and design elements we hope to incorporate.
-We also recognize there is no substitute for creativity and originality.

Favorite Website Design Examples:

http://www.joggingwithmarla.example/
HD backgrounds are a plus.
These colors are great.
The bright splashes of blue, red and orange combined with black in these shades.
A predominant background of whitesmoke or beige.

https://tillbrook.example/
The HD backgrounds are sharp.
The look is very clean (though it has a slight Pearfield computers imitation).
The left to right “scrolling” is preferable to vertical scrolling.
Very pleasing to the eye.

http://www.gravelpathworks.example/
Again, use of bright, vibrant HD graphics is exceptional.
The left to right scrolling navigation is slick and likely how we would like our services to flow.

http://buzzing.visitlakeshore.example/
Love the look, feel and concepts in this site’s design
Especially colors and “photography” elements.
Updates

We've seen a few common themes in various designs submitted so far and want to add a few suggestions as we enter the final week of our design contest.

We do not want any photos of healthcare professionals or close-ups of people (families or couples or individuals).  Although we are a health care company we don't want to fall into a cliche feel for our site.  Instead we would like either objects or abstract images that have depth and are high definition, spanning from edge to edge of the width of the screen. 

We prefer shades of grey for the base color scheme with highlights of bright colors.  Please refer to the examples on the brief and use those as the best guide of what we want.  Even SketchHive's color scheme is closer to what we want than some of the submissions, so please take note of the "shades of grey" with splashes of bright accent colors.

We love the horizontal navigation bar like that seen in the gravel-path works site and anticipate our final product using a similar transition between the functions of the site.

Good luck to you all.  We are still looking for that WOW factor and hoping to see something original, that breaks the traditional mold and has a feel like the examples posted.  

Industry/Entity Type

Communication

```html
<!DOCTYPE html>
<html lang="en">
<head>
<meta charset="utf-8">
<title>Ledger Loom — Home</title>
<link rel="stylesheet" href="https://fonts.googleapis.com/css2?family=Open+Sans:wght@300;400;600;700&display=swap">
<style>
  :root {
    --navy: #1f2f63;
    --navy-deep: #15214a;
    --orange: #f09a12;
    --orange-deep: #d9780a;
    --text-grey: #555a60;
    --soft-grey: #8a8f96;
    --panel: rgba(255,255,255,0.92);
    --nav-bg: #f3f4f5;
    --nav-active: #dfe1e4;
    --arrow-bg: #3a3d42;
    --sky-top: #d8ecf8;
    --sky-mid: #9fcbe8;
    --grass-light: #a9cf3a;
    --grass-dark: #5f8f1c;
  }
  * { box-sizing: border-box; margin: 0; padding: 0; }
  html, body { width: 1200px; height: 517px; overflow: hidden; }
  body { font-family: "Open Sans", Arial, sans-serif; position: relative; }

  .hero-backdrop {
    position: absolute; inset: 0;
    background:
      radial-gradient(ellipse 330px 300px at 600px 200px, var(--sky-top) 0%, var(--sky-mid) 55%, rgba(159,203,232,0) 100%),
      radial-gradient(ellipse 720px 500px at 600px 240px, #b7d9a0 0%, var(--grass-light) 55%, var(--grass-dark) 100%);
  }

  .brand { position: absolute; left: 469px; top: 16px; display: flex; align-items: center; gap: 9px; }
  .brand-square { width: 44px; height: 44px; background: var(--navy); border-radius: 5px; }
  .brand-name { font-size: 31px; font-weight: 300; color: var(--navy); letter-spacing: 0.5px; text-transform: uppercase; }

  .main-nav {
    position: absolute; left: 255px; top: 79px; width: 689px; height: 26px;
    background: var(--nav-bg); display: flex; font-size: 11px; color: #333;
    box-shadow: 0 1px 2px rgba(0,0,0,0.15);
  }
  .main-nav a { color: inherit; text-decoration: none; padding: 0 11px; line-height: 26px; }
  .main-nav a.is-active { background: var(--nav-active); }
  .main-nav .sign-in { margin-left: auto; background: var(--navy-deep); color: #fff; width: 99px; text-align: center; }
  .sign-in b { color: var(--orange); font-weight: 400; }

  .account-panel {
    position: absolute; left: 255px; top: 120px; width: 302px; height: 231px;
    background: var(--panel); border-radius: 3px; padding: 12px 12px;
    box-shadow: 0 1px 4px rgba(0,0,0,0.2);
  }
  .tagline-accent { color: var(--orange); font-size: 22px; font-weight: 400; line-height: 24px; }
  .tagline-accent span { color: var(--navy); font-weight: 300; }
  .tagline-main { color: var(--navy); font-size: 27px; font-weight: 300; line-height: 30px; }
  .form-title { margin-top: 14px; padding-bottom: 5px; font-size: 13px; color: #444; border-bottom: 1px solid #ccc; }
  .field { display: flex; align-items: center; margin-top: 6px; font-size: 10px; color: #444; }
  .field:first-of-type { margin-top: 12px; }
  .field label { width: 86px; text-align: right; padding-right: 6px; }
  .field input { width: 180px; height: 18px; border: 1px solid #c9cbce; background: #f1f2f3; }
  .register-btn {
    margin: 11px 0 0 86px; width: 114px; height: 27px; border: 0; border-radius: 2px;
    background: linear-gradient(var(--orange), var(--orange-deep)); color: #fff;
    font-family: inherit; font-size: 12px; text-transform: uppercase;
  }

  .intro { position: absolute; left: 575px; top: 130px; width: 300px; }
  .intro h2 { font-size: 22px; font-weight: 300; color: #6a6f75; line-height: 26px; }
  .intro p { margin-top: 6px; font-size: 9.5px; line-height: 12.5px; color: var(--text-grey); width: 270px; }
  .intro .more { display: flex; align-items: center; gap: 6px; margin-top: 13px; font-size: 10px; font-weight: 700; color: var(--orange); }
  .more i { width: 13px; height: 13px; border-radius: 50%; background: var(--orange); display: inline-block; }

  .next-slide { position: absolute; left: 896px; top: 220px; width: 48px; height: 47px; background: var(--arrow-bg); border-radius: 3px 0 0 3px; }

  .service-band {
    position: absolute; left: 255px; top: 372px; width: 689px; height: 75px;
    background: linear-gradient(#26397a, var(--navy-deep)); border-radius: 3px;
    display: flex;
  }
  .service { flex: 1; display: flex; align-items: center; padding-left: 16px; gap: 12px; position: relative; }
  .service svg.icon { flex: none; }
  .service-label { color: #fff; font-size: 20px; font-weight: 300; line-height: 22px; text-transform: uppercase; }
  .service-label strong { display: block; color: var(--orange); font-weight: 600; }
  .chevron { position: absolute; right: -10px; top: 0; z-index: 1; }

  .site-footer { position: absolute; left: 271px; top: 470px; font-size: 10px; color: #2a2a2a; line-height: 15px; }
  .site-footer a { color: inherit; text-decoration: none; }
  .social { position: absolute; left: 853px; top: 471px; display: flex; gap: 4px; }
  .social span { width: 22px; height: 22px; border-radius: 50%; background: #fff; border: 2px solid #d7dade; }
</style>
</head>
<body>
  <div class="hero-backdrop" role="img" aria-label="Wide fisheye photo of children running on a curved green lawn under a bright blue sky"></div>

  <header class="brand">
    <span class="brand-square"></span>
    <span class="brand-name">Ledger Loom</span>
  </header>

  <nav class="main-nav">
    <a href="#" class="is-active">HOME</a>
    <a href="#">ABOUT US</a>
    <a href="#">FAQ</a>
    <a href="#">CONTACT US</a>
    <a href="#" class="sign-in"><b>SIGN IN</b> HERE</a>
  </nav>

  <section class="account-panel">
    <div class="tagline-accent">WE PLANS <span>FOR</span></div>
    <div class="tagline-main">MEDICAL MARKET...</div>
    <div class="form-title">Create Account</div>
    <div class="field"><label>Email:</label><input type="text"></div>
    <div class="field"><label>Password:</label><input type="password"></div>
    <div class="field"><label>Re-type Password:</label><input type="password"></div>
    <button class="register-btn">Register Now</button>
  </section>

  <section class="intro">
    <h2>Neque porro quisquam est qui dolorem ipsum quia dolor sit amet, consectetur...</h2>
    <p>There are many variations of passages of Lorem Ipsum available, but the majority have suffered alteration in some form, by injected humour, or randomised words which don't look even slightly believable.</p>
    <div class="more"><i></i>Lorem Ipsum</div>
  </section>

  <a class="next-slide" href="#" aria-label="Next slide">
    <svg width="48" height="47" viewBox="0 0 48 47"><path d="M20 14 L29 23.5 L20 33" fill="none" stroke="#fff" stroke-width="4"/></svg>
  </a>

  <section class="service-band">
    <div class="service">
      <svg class="icon" width="44" height="44" viewBox="0 0 44 44"><circle cx="17" cy="17" r="12" fill="#cfe6f7" stroke="#9fb6c8" stroke-width="3"/><path d="M26 26 L39 39" stroke="#e8a020" stroke-width="6" stroke-linecap="round"/></svg>
      <div class="service-label"><strong>Search</strong>for a loan</div>
      <svg class="chevron" width="20" height="75" viewBox="0 0 20 75"><path d="M0 0 L18 37.5 L0 75" fill="none" stroke="#3a4e90" stroke-width="2"/></svg>
    </div>
    <div class="service">
      <svg class="icon" width="52" height="40" viewBox="0 0 52 40"><rect x="2" y="4" width="38" height="24" rx="3" fill="#5aa6d8"/><rect x="12" y="12" width="38" height="24" rx="3" fill="#5fc070"/></svg>
      <div class="service-label"><strong>Create</strong>a payment plan</div>
      <svg class="chevron" width="20" height="75" viewBox="0 0 20 75"><path d="M0 0 L18 37.5 L0 75" fill="none" stroke="#3a4e90" stroke-width="2"/></svg>
    </div>
    <div class="service">
      <svg class="icon" width="46" height="50" viewBox="0 0 46 50"><rect x="8" y="2" width="26" height="16" rx="2" fill="#7a2440"/><rect x="4" y="16" width="38" height="30" rx="4" fill="#e6e8ea"/><rect x="10" y="22" width="26" height="18" rx="2" fill="#b9bdc2"/></svg>
      <div class="service-label"><strong>Make</strong>a payment</div>
    </div>
  </section>

  <footer class="site-footer">
    <div><a href="#">Home</a> | <a href="#">About us</a> | <a href="#">Faq</a> | <a href="#">Contact us</a></div>
    <div>© 2012 Ledger Loom. All rights reserved.</div>
  </footer>

  <div class="social">
    <span role="img" aria-label="Kindred Link"></span>
    <span role="img" aria-label="Chirpline"></span>
    <span role="img" aria-label="Orbit Plus"></span>
  </div>
</body>
</html>
```